New business card design needed for Trucking/Staffing company!

I am looking for a business card design. The business name is Harbor Lane Freightworks, LLC. This company is a staffing company for commercial drivers/truck drivers. Most of our customers are trucking/supply companies. Our colors are blue/black/white/grey. The info I have on my current business cards is
-Spot for a name
-2 lines for an address
-3 lines for Office, cell, and fax
-email
-website(currently on backside of card with logo but can go anywhere)
Updates

Project Deadline Extended
Reason: Open to more designs

Target Market(s)

Trucking companies, building supply companies

Industry/Entity Type

Business

Contact Information for Business Card

Edgy but professional

Font styles to use
Other font styles liked:
• Open to suggestions

Colors
0555a3
000000
ffffff
9d9d9d

Requirements
Must have
• Must have the logo incorporated

```html
<!DOCTYPE html>
<html lang="en">
<head>
<meta charset="utf-8">
<title>Harbor Lane Freightworks – Business Card</title>
<link href="https://fonts.googleapis.com/css2?family=Michroma&family=Exo+2:wght@300&display=swap" rel="stylesheet">
<style>
  :root {
    --backdrop: #262626;
    --card-white: #ffffff;
    --card-black: #060708;
    --panel-black: #000000;
    --ink: #111111;
    --brand-blue: #2b3a9c;
    --paper-text: #ffffff;
  }
  html, body {
    margin: 0;
    padding: 0;
    width: 1200px;
    height: 1200px;
    overflow: hidden;
    background: var(--backdrop);
  }
  .canvas {
    position: relative;
    width: 1200px;
    height: 1200px;
  }
  .card {
    position: absolute;
    width: 782px;
    height: 459px;
    overflow: hidden;
  }
  .card-front {
    left: 149px;
    top: 93px;
    background: var(--card-white);
  }
  .card-back {
    left: 269px;
    top: 648px;
    background: var(--card-black);
  }
  .brand-name {
    position: absolute;
    margin: 0;
    font-family: "Michroma", sans-serif;
    font-weight: 400;
    color: var(--brand-blue);
    text-transform: uppercase;
    line-height: 1.25;
  }
  .card-front .brand-name {
    left: 51px;
    top: 72px;
    font-size: 25px;
    letter-spacing: 1px;
  }
  .holder-name {
    position: absolute;
    left: 371px;
    top: 255px;
    margin: 0;
    font-family: "Michroma", sans-serif;
    font-weight: 400;
    font-size: 25px;
    letter-spacing: 4px;
    color: var(--ink);
    text-transform: uppercase;
  }
  .contact {
    position: absolute;
    top: 304px;
    margin: 0;
    padding: 0;
    list-style: none;
    font-family: "Exo 2", sans-serif;
    font-weight: 300;
    font-size: 24px;
    line-height: 38px;
    color: var(--ink);
    text-transform: uppercase;
    letter-spacing: 0.5px;
  }
  .contact-phones { left: 59px; }
  .contact-address { left: 371px; }
  .back-panel {
    position: absolute;
    left: 313px;
    top: 130px;
    right: 0;
    bottom: 0;
    background: var(--panel-black);
  }
  .website {
    position: absolute;
    left: 59px;
    top: 364px;
    margin: 0;
    font-family: "Michroma", sans-serif;
    font-size: 14px;
    letter-spacing: 3px;
    color: var(--paper-text);
    text-transform: uppercase;
  }
  .card-back .brand-name {
    right: 42px;
    top: 338px;
    font-size: 17px;
    text-align: right;
    letter-spacing: 1px;
  }
</style>
</head>
<body>
<main class="canvas">
  <section class="card card-front" aria-label="Business card front">
    <h1 class="brand-name">Harbor Lane<br>Freightworks</h1>
    <h2 class="holder-name">John&nbsp; Doe</h2>
    <ul class="contact contact-phones">
      <li>T: 1(800)555-0142</li>
      <li>T: (555)201-3387</li>
      <li>F: (555)201-3390</li>
    </ul>
    <ul class="contact contact-address">
      <li>1180 Dockside Rd.</li>
      <li>Millbrook, TX 78012</li>
      <li>dana@harborlanefw.com</li>
    </ul>
  </section>

  <section class="card card-back" aria-label="Business card back">
    <div class="back-panel"></div>
    <p class="website">www.harborlanefw.com</p>
    <p class="brand-name">Harbor Lane<br>Freightworks</p>
  </section>
</main>
</body>
</html>
```